Clay Sparrow- Hand made fashion accessories

Clay sparrow is a new business that will be selling hand made fashion accessories for women such as bags, baskets, knecklaces etc. The items are all hand made from Africa. I would like natural colors leaning more to the cardboard rustic look. I would like the card to look simple but elegant at the same time.

Industry/Entity Type

Business

Contact Information for Business Card

www.claysparrow-example.com.au
sales@claysparrow-example.com.au
Tel: 0452867310

Font styles to use
Decorative
Script

Requirements
Must have
• Earthy and rustic colours. Straw, cardboard etc. Fine black cursive print. One side of card only name
• second side website, email and tel.
Should not have
• No need to have any description of what business sells or does. No pictures of anything.

```html
<!DOCTYPE html>
<html lang="en">
<head>
<meta charset="utf-8">
<title>Clay Sparrow – Business Card</title>
<link href="https://fonts.googleapis.com/css2?family=Handlee&display=swap" rel="stylesheet">
<style>
  :root {
    --page: #ecebe8;
    --ink: #5b3a22;
    --ink-soft: #6e4a2e;
    --card-light: #efd3ad;
    --card-mid: #e2c197;
    --front-light: #e0c59f;
    --front-mid: #c8a477;
    --front-dark: #9f7a4f;
    --seal-light: #f0d9b8;
    --seal-edge: #d9b88c;
  }
  * { margin: 0; padding: 0; box-sizing: border-box; }
  html, body {
    width: 1200px;
    height: 800px;
    overflow: hidden;
    background: var(--page);
  }
  .sheet {
    width: 1200px;
    height: 800px;
    display: flex;
    align-items: center;
    justify-content: center;
    gap: 44px;
  }
  .card {
    width: 530px;
    height: 303px;
    border-radius: 3px;
    box-shadow: 0 6px 18px rgba(60, 40, 20, 0.18);
    position: relative;
    font-family: "Handlee", cursive;
    color: var(--ink);
  }
  /* Back side – contact details */
  .card--contact {
    background: linear-gradient(160deg, var(--card-light) 0%, var(--card-mid) 100%);
    display: flex;
    align-items: center;
    justify-content: center;
  }
  .contact-list {
    list-style: none;
    display: flex;
    flex-direction: column;
    gap: 16px;
  }
  .contact-item {
    display: flex;
    align-items: center;
    gap: 14px;
    font-size: 21px;
    letter-spacing: 0.3px;
  }
  .contact-icon {
    width: 20px;
    height: 20px;
    flex: none;
    fill: var(--ink);
  }
  /* Front side – name */
  .card--name {
    background:
      radial-gradient(ellipse at 45% 40%, var(--front-light) 0%, var(--front-mid) 55%, var(--front-dark) 100%);
    display: flex;
    align-items: center;
    justify-content: center;
  }
  .name-seal {
    width: 200px;
    height: 200px;
    border-radius: 50%;
    border: 1.5px solid var(--ink-soft);
    background: radial-gradient(circle at 50% 45%, var(--seal-light) 0%, var(--seal-edge) 100%);
    display: flex;
    align-items: center;
    justify-content: center;
    text-align: center;
  }
  .brand-name {
    font-size: 36px;
    font-weight: 400;
    line-height: 1.1;
    color: var(--ink);
  }
</style>
</head>
<body>
  <main class="sheet">
    <section class="card card--contact" aria-label="Contact side">
      <ul class="contact-list">
        <li class="contact-item">
          <svg class="contact-icon" viewBox="0 0 24 24" aria-hidden="true">
            <path d="M6.6 10.8a15.1 15.1 0 0 0 6.6 6.6l2.2-2.2a1 1 0 0 1 1-.25 11.4 11.4 0 0 0 3.6.57 1 1 0 0 1 1 1V20a1 1 0 0 1-1 1A17 17 0 0 1 3 4a1 1 0 0 1 1-1h3.5a1 1 0 0 1 1 1c0 1.25.2 2.45.57 3.57a1 1 0 0 1-.25 1z"/>
          </svg>
          <span>0452867310</span>
        </li>
        <li class="contact-item">
          <svg class="contact-icon" viewBox="0 0 24 24" aria-hidden="true">
            <path d="M3 5h18a1 1 0 0 1 1 1v12a1 1 0 0 1-1 1H3a1 1 0 0 1-1-1V6a1 1 0 0 1 1-1zm.8 1.6L12 12.4l8.2-5.8H3.8zM20.4 8.2 12 14.2 3.6 8.2v9.2h16.8z"/>
          </svg>
          <span>sales@claysparrow-example.com.au</span>
        </li>
        <li class="contact-item">
          <svg class="contact-icon" viewBox="0 0 24 24" aria-hidden="true">
            <path d="M12 2a10 10 0 1 0 0 20 10 10 0 0 0 0-20zm6.9 9h-3a15 15 0 0 0-1.3-5.6A8 8 0 0 1 18.9 11zM12 4.1c.9 1.2 1.8 3.6 2 6.9h-4c.2-3.3 1.1-5.7 2-6.9zM9.4 5.4A15 15 0 0 0 8.1 11h-3a8 8 0 0 1 4.3-5.6zM5.1 13h3a15 15 0 0 0 1.3 5.6A8 8 0 0 1 5.1 13zm6.9 6.9c-.9-1.2-1.8-3.6-2-6.9h4c-.2 3.3-1.1 5.7-2 6.9zm2.6-1.3a15 15 0 0 0 1.3-5.6h3a8 8 0 0 1-4.3 5.6z"/>
          </svg>
          <span>www.claysparrow-example.com.au</span>
        </li>
      </ul>
    </section>

    <section class="card card--name" aria-label="Name side">
      <div class="name-seal">
        <h1 class="brand-name">Clay<br>Sparrow</h1>
      </div>
    </section>
  </main>
</body>
</html>
```